New Business Card for Casual Beachfront Cafe

Quirky Beachfront Cafe at Moana, South Australia needs a DOUBLE SIDED business card to print on PrintHarbor.

Target Market(s)

Business Cards sit on the counter for Guests to take with them. Please view our website www.saltreefcafe.com.au to get a feel for the Cafe. You may also view our Instagram at @saltreefcafe

Industry/Entity Type

Cafe / Restaurant

Contact Information for Business Card

Information equivalent to: Breakfast, Lunch, Dinner, Coffee, Takeaway / 117 Parade Kelpwater SA 5912 / Menu & Opening Hours: www.saltreefcafe.com.au / ph (08) 8461 9273

Requirements
Must have
• Information equivalent to: Breakfast, Lunch, Dinner, Coffee, Takeaway / 117 Parade Kelpwater SA 5912 / Menu & Opening Hours: www.saltreefcafe.com.au / ph (08) 8461 9273
Nice to have
• Potentially some of our trademark colours (Cafe can be searched via Seekly)
Should not have
• Must NOT have image of the building. May have the logo provided on one side but not necessarily, depending on how you wish to design the card

```html
<!DOCTYPE html>
<html lang="en">
<head>
<meta charset="utf-8">
<title>Salt Reef Cafe – Business Card</title>
<link rel="stylesheet" href="https://fonts.googleapis.com/css2?family=Montserrat+Alternates:wght@500;600;800&display=swap">
<style>
  :root {
    --bg-top: #8a8a8a;
    --bg-bottom: #6a6a6a;
    --yellow: #f7f50c;
    --brown: #b35817;
    --blue: #17468a;
    --blue-deep: #0b3670;
    --white: #f2f4f8;
    --orange: #c9641e;
  }
  * { box-sizing: border-box; margin: 0; padding: 0; }
  html, body { width: 1200px; height: 915px; overflow: hidden; }
  body {
    background: linear-gradient(var(--bg-top), var(--bg-bottom));
    font-family: "Montserrat Alternates", sans-serif;
    position: relative;
  }
  .card {
    position: absolute;
    top: 303px;
    width: 540px;
    height: 309px;
    box-shadow: 0 18px 40px rgba(0,0,0,0.35);
    overflow: hidden;
  }
  .card--front { left: 630px; background: var(--brown); }
  .card--back  { left: 30px;  background: linear-gradient(var(--blue), var(--blue-deep)); }

  /* Front */
  .front-panel {
    position: absolute;
    inset: 32px 36px;
    background: var(--yellow);
    display: flex;
    flex-direction: column;
    align-items: center;
    justify-content: center;
  }
  .front-name {
    color: var(--blue);
    font-weight: 800;
    font-size: 50px;
    line-height: 1.05;
    text-align: center;
    text-transform: uppercase;
    letter-spacing: 1px;
  }

  /* Back */
  .back-band {
    position: absolute;
    top: 0; left: 0; right: 0;
    height: 62px;
    background: var(--yellow);
  }
  .back-badge {
    position: absolute;
    top: 40px; left: 270px;
    width: 138px; height: 66px;
    background: var(--yellow);
    border: 4px solid var(--brown);
    display: flex;
    align-items: center;
    justify-content: center;
  }
  .back-badge-name {
    color: var(--blue);
    font-weight: 800;
    font-size: 17px;
    line-height: 1.05;
    text-align: center;
    text-transform: uppercase;
  }
  .back-info {
    position: absolute;
    left: 34px; top: 120px;
    right: 20px;
    color: var(--white);
    font-size: 15px;
    font-weight: 500;
    line-height: 1.55;
  }
  .info-services, .info-label {
    color: var(--yellow);
    font-weight: 600;
  }
  .info-services { font-size: 17px; margin-bottom: 6px; white-space: nowrap; }
  .info-row { display: flex; align-items: center; gap: 10px; }
  .info-row svg { width: 14px; height: 14px; flex: none; }
  .info-indent { padding-left: 24px; }
</style>
</head>
<body>

  <section class="card card--back" aria-label="Business card, back">
    <div class="back-band"></div>
    <div class="back-badge">
      <span class="back-badge-name">Salt Reef<br>Cafe</span>
    </div>
    <div class="back-info">
      <p class="info-services">Breakfast, Lunch, Dinner, Coffee, Takeaway</p>
      <p class="info-row">
        <svg viewBox="0 0 24 24" aria-hidden="true"><path fill="var(--orange)" d="M12 2a7 7 0 0 0-7 7c0 5 7 13 7 13s7-8 7-13a7 7 0 0 0-7-7zm0 9.5A2.5 2.5 0 1 1 12 6.5a2.5 2.5 0 0 1 0 5z"/></svg>
        117 Parade Kelpwater SA 5912
      </p>
      <p class="info-label info-indent">Menu &amp; Opening Hours:</p>
      <p class="info-row">
        <svg viewBox="0 0 24 24" aria-hidden="true"><g fill="none" stroke="var(--orange)" stroke-width="2"><circle cx="12" cy="12" r="9"/><path d="M3 12h18M12 3c3 3 3 15 0 18M12 3c-3 3-3 15 0 18"/></g></svg>
        www.saltreefcafe.com.au
      </p>
      <p class="info-row">
        <svg viewBox="0 0 24 24" aria-hidden="true"><path fill="var(--orange)" d="M6.6 10.8a15 15 0 0 0 6.6 6.6l2.2-2.2a1 1 0 0 1 1-.25 11.4 11.4 0 0 0 3.6.57 1 1 0 0 1 1 1V20a1 1 0 0 1-1 1A17 17 0 0 1 3 4a1 1 0 0 1 1-1h3.5a1 1 0 0 1 1 1c0 1.25.2 2.45.57 3.6a1 1 0 0 1-.25 1z"/></svg>
        (08) 8461 9273
      </p>
    </div>
  </section>

  <section class="card card--front" aria-label="Business card, front">
    <div class="front-panel">
      <h1 class="front-name">Salt Reef<br>Cafe</h1>
    </div>
  </section>

</body>
</html>
```